Larkfield Rowhomes - Billboard design for our newly renovated townhome community

We have a 5' wide x 4' tall billboard at the entrance to our apartment community, that needs to have the acrylic insert replaced. It is a 2 sided sign, and we are planning to use the same image on both sides. We are called Larkfield Rowhomes, and have 48 townhomes that are all 2 bedroom, 1 1/2 bath. A few things we would like to get across on the signage: "Newly Renovated" "2 bed 1 1/2 bath" "Full size W/D in every home" " New Appliances" I've included our parent company's logo - this is the only image I could think of, but it might not be worth having it on the sign. We are in Colorado, so mountain theme could be nice and also sunshine/sun since we are called "Larkfield"

Industry/Entity Type

Apartment

Font styles to use
Sans Serif

Requirements
Must have
• Newly Renovated
2 bed 1 1/2 bath
Full size W/D in every home
Virtual Tours available
www.brambletonhomesco.example
855 - 413 - 9286
Nice to have
• We are located in Colorado - possibly mountain theme? Since our community is called "Larkfield Rowhomes" - anything bright with Sun / Sunshine might look really nice as well.

```html
<!DOCTYPE html>
<html lang="en">
<head>
<meta charset="utf-8">
<title>Larkfield Rowhomes – Entrance Sign</title>
<link rel="stylesheet" href="https://fonts.googleapis.com/css2?family=Bebas+Neue&family=Oswald:wght@500;600&display=swap">
<style>
  :root {
    --stage: #1b1b1d;
    --sky-top: #1f86d6;
    --sky-low: #8cc6ea;
    --rock-light: #c98a5a;
    --rock-deep: #a4532c;
    --title-red: #e8202a;
    --title-edge: #f6e51b;
    --badge-red: #e51f2b;
    --badge-edge: #f6e51b;
    --ink: #111111;
    --band: #000000;
    --band-text: #ffffff;
    --strip: rgba(200, 228, 245, 0.55);
  }
  * { margin: 0; padding: 0; box-sizing: border-box; }
  html, body {
    width: 1200px; height: 479px; overflow: hidden;
    background: var(--stage);
  }
  .sign {
    position: absolute; left: 300px; top: 0;
    width: 599px; height: 479px; overflow: hidden;
    font-family: "Bebas Neue", "Oswald", sans-serif;
  }
  .sign__scene {
    position: absolute; inset: 0 0 44px 0;
    background:
      linear-gradient(180deg, var(--sky-top) 0%, var(--sky-low) 46%, var(--rock-light) 56%, var(--rock-deep) 78%, #b46a3f 100%);
  }
  .sign__title {
    position: absolute; left: 0; right: 0; top: 6px;
    text-align: center;
    color: var(--title-red);
    font-size: 104px; line-height: 82px; letter-spacing: 1px;
    -webkit-text-stroke: 2px var(--title-edge);
    paint-order: stroke fill;
  }
  .sign__features {
    position: absolute; left: 53px; width: 493px; top: 182px; height: 33px;
    background: var(--strip);
    display: flex; align-items: center; justify-content: center; gap: 8px;
    font-family: "Oswald", sans-serif; font-weight: 600;
    font-size: 16px; color: var(--ink); text-transform: uppercase;
    letter-spacing: -0.2px;
  }
  .sign__divider { color: var(--title-edge); font-weight: 500; }
  .sign__badge {
    position: absolute; left: 256px; top: 216px; width: 102px; height: 102px;
  }
  .sign__badge-text {
    position: absolute; left: 256px; top: 233px; width: 102px;
    text-align: center; color: var(--title-edge);
    transform: rotate(4deg);
  }
  .sign__badge-text .big { display: block; font-size: 24px; line-height: 20px; }
  .sign__badge-text .small {
    display: block; font-family: "Oswald", sans-serif; font-weight: 500;
    font-size: 13px; line-height: 16px;
  }
  .sign__contact {
    position: absolute; left: 0; right: 0; bottom: 0; height: 44px;
    background: var(--band); color: var(--band-text);
    display: flex; align-items: center; justify-content: center; gap: 12px;
    font-size: 27px; letter-spacing: 0.5px;
  }
</style>
</head>
<body>
  <section class="sign">
    <div class="sign__scene" role="img" aria-label="Photo of red sandstone rock formations and desert valley under a clear blue sky"></div>

    <h1 class="sign__title">LARKFIELD<br>ROWHOMES</h1>

    <p class="sign__features">
      <span>Newly Renovated</span><span class="sign__divider">|</span>
      <span>2 Bed 1½ Bath</span><span class="sign__divider">|</span>
      <span>Full Size W/D in Every Home</span>
    </p>

    <svg class="sign__badge" viewBox="0 0 102 102" aria-hidden="true">
      <path d="M10 6 L92 14 Q98 15 97 22 L92 78 Q91 84 85 86 L42 98 Q36 100 33 95 L4 22 Q2 8 10 6 Z"
            fill="var(--badge-red)" stroke="var(--badge-edge)" stroke-width="3" stroke-linejoin="round"/>
    </svg>
    <p class="sign__badge-text">
      <span class="big">VIRTUAL<br>TOURS</span>
      <span class="small">AVAILABLE</span>
    </p>

    <footer class="sign__contact">
      <span>WWW.BRAMBLETONHOMESCO.EXAMPLE</span><span>|</span><span>855 - 413 - 9286</span>
    </footer>
  </section>
</body>
</html>
```